create a book cover titled "bright canyon drift"

>>>>Updated Description>>>>>
I need conceptually enriched and minimal book cover design that hopefully represents the theme on the front page, The book is about romanticizing greenery and forests. It's a novel based on life of botanical creatures and their interaction. Think of it as a role playing novel where you(the reader) will be experiencing the story and life of botany. Book is also accompanied by a series of soundtracks which will be embedded through some secondary medium within the book.
- The cover should be simple and very minimal and could be orignal illustration
- Only design front cover, inner content and back cover design details will be shared with the winning designer only.
- Don't do any ornamanation
- It should be very too the point and clean
- hit me up incase of any confusions and ask me to clarify anything, I am here to help you out,feel free to post but design isn't really my thing so you've 100% creative freedom, I just want the design of the book cover to represent my ideas visually.
- dimensions 5.5x8

Please view the updated brief. Please alter your designs accordingly. Best Regards

Target Market(s)

adults

Font styles to use
Serif
Sans Serif

Colors

Designer to choose colors to be used in the design.

Requirements
Must have
• - Minimal design
• - Clean text
• - Bold Imagery
Nice to have
• Illustrations
Should not have
• - Dark colors
• - something abstract
• - Contentless elements

```html
<!DOCTYPE html>
<html lang="en">
<head>
<meta charset="utf-8">
<title>Bright Canyon Drift — Book Cover</title>
<link rel="stylesheet" href="https://fonts.googleapis.com/css2?family=Oswald:wght@600;700&display=swap">
<style>
  :root {
    --backdrop: #e9eaec;
    --paper: #ffffff;
    --title: #ffffff;
    --forest-light: #6fbf2c;
    --forest-mid: #3f8f1c;
    --forest-deep: #1f4d12;
    --bark-light: #cfcfcf;
    --bark-dark: #767676;
  }
  html, body {
    margin: 0;
    padding: 0;
    overflow: hidden;
  }
  body {
    width: 1200px;
    height: 800px;
    background: var(--backdrop);
    display: flex;
    align-items: center;
    justify-content: center;
  }
  .book-cover {
    width: 522px;
    height: 760px;
    background: var(--paper);
    box-shadow: 0 10px 30px rgba(0, 0, 0, 0.18);
    overflow: hidden;
  }
  .book-cover svg {
    display: block;
    width: 100%;
    height: 100%;
  }
  .title-word {
    font-family: "Oswald", "Arial Narrow", sans-serif;
    font-weight: 700;
    fill: var(--title);
  }
  .title-word--middle {
    font-weight: 600;
  }
</style>
</head>
<body>
  <main class="book-cover">
    <svg viewBox="0 0 522 760" xmlns="http://www.w3.org/2000/svg">
      <defs>
        <linearGradient id="forestGradient" x1="0" y1="0" x2="0" y2="1">
          <stop offset="0" stop-color="var(--forest-deep)"/>
          <stop offset="0.35" stop-color="var(--forest-mid)"/>
          <stop offset="1" stop-color="var(--forest-light)"/>
        </linearGradient>
        <linearGradient id="barkGradient" x1="0" y1="0" x2="1" y2="0">
          <stop offset="0" stop-color="var(--bark-dark)"/>
          <stop offset="0.5" stop-color="var(--bark-light)"/>
          <stop offset="1" stop-color="var(--bark-dark)"/>
        </linearGradient>
      </defs>

      <rect class="cover-paper" x="0" y="0" width="522" height="760" fill="var(--paper)"/>

      <rect class="band-top" x="22" y="14" width="500" height="76" fill="url(#barkGradient)"
            role="img" aria-label="Grey-toned strip of forest tree trunks"/>

      <rect class="forest-photo" x="22" y="90" width="500" height="510" fill="url(#forestGradient)"
            role="img" aria-label="Photograph of a mossy green forest floor with a hooded walker among tall trunks"/>

      <rect class="band-bottom" x="22" y="600" width="500" height="160" fill="url(#barkGradient)"
            role="img" aria-label="Grey-toned strip of tangled forest roots"/>

      <text class="title-word title-word--top" x="18" y="222" font-size="240" textLength="486" lengthAdjust="spacingAndGlyphs">BRIGHT</text>
      <text class="title-word title-word--middle" x="54" y="432" font-size="140" textLength="420" lengthAdjust="spacingAndGlyphs">CANYON</text>
      <text class="title-word title-word--bottom" x="18" y="752" font-size="244" textLength="486" lengthAdjust="spacingAndGlyphs">DRIFT</text>
    </svg>
  </main>
</body>
</html>
```